Real Estate Entrepreneur needs a business card

I am a real estate entrepreneur, I buy houses for investment purposes, I act as a real estate agent representing buyers and sellers in residential home transactions, I am a contractor that does a wide range of home repairs and construction. I'd like a design that can stick with me through the years as my business grows and morphs to fit any niche I decide to pursue as markets change.

Target Market(s)

Anyone with interest that may be related to real estate.

Industry/Entity Type

Real Estate

Contact Information for Business Card

A card that stands out and doesn't put me in any one box. My business will evolve over time and I need a card that can stay relevant.

Colors

Designer to choose colors to be used in the design.

Requirements
Must have
• Character
Nice to have
• I'm open
Should not have
• Cliche houses and hammers

```html
<!DOCTYPE html>
<html lang="en">
<head>
<meta charset="utf-8">
<title>Reid Calder – Business Card</title>
<link rel="stylesheet" href="https://fonts.googleapis.com/css2?family=Montserrat:wght@300;400;600&display=swap">
<style>
  :root {
    --backdrop: #262626;
    --card: #141414;
    --card-edge: #1c1c1c;
    --foil: #8c8c8c;
    --foil-soft: #6f6f6f;
    --rule: #5c5c5c;
  }
  * { box-sizing: border-box; margin: 0; padding: 0; }
  html, body {
    width: 1200px;
    height: 550px;
    overflow: hidden;
    background: var(--backdrop);
    font-family: "Montserrat", Arial, sans-serif;
  }
  .canvas {
    width: 1200px;
    height: 550px;
    display: flex;
    align-items: center;
    justify-content: center;
    gap: 80px;
  }
  .card {
    width: 500px;
    height: 286px;
    background: var(--card);
    border: 1px solid var(--card-edge);
    border-radius: 3px;
    box-shadow: 0 18px 40px rgba(0,0,0,.45);
    position: relative;
  }

  /* Front side */
  .card-front {
    display: flex;
    align-items: center;
    padding-left: 62px;
  }
  .identity { width: 168px; }
  .identity .name {
    font-size: 26px;
    font-weight: 400;
    color: var(--foil);
    letter-spacing: .2px;
    line-height: 1;
  }
  .identity .role {
    margin-top: 6px;
    font-size: 9px;
    font-weight: 400;
    letter-spacing: 1.2px;
    color: var(--foil-soft);
  }
  .divider {
    width: 1px;
    height: 70px;
    background: var(--rule);
    margin: 0 22px 0 4px;
  }
  .contact-list { list-style: none; }
  .contact-list li {
    display: flex;
    align-items: center;
    gap: 8px;
    font-size: 10.5px;
    color: var(--foil-soft);
    line-height: 1;
    margin: 7px 0;
  }
  .contact-list svg { width: 10px; height: 10px; fill: var(--foil-soft); flex: none; }

  /* Back side */
  .card-back {
    display: flex;
    flex-direction: column;
    align-items: center;
    justify-content: center;
    gap: 18px;
  }
  .brand-square {
    width: 58px;
    height: 58px;
    background: var(--foil);
  }
  .brand-name {
    font-size: 44px;
    font-weight: 400;
    color: var(--foil);
    letter-spacing: .5px;
    line-height: 1;
  }
</style>
</head>
<body>
<main class="canvas">

  <section class="card card-front" aria-label="Card front">
    <div class="identity">
      <p class="name">Reid Calder</p>
      <p class="role">REALTOR</p>
    </div>
    <span class="divider"></span>
    <ul class="contact-list">
      <li>
        <svg viewBox="0 0 10 10" aria-hidden="true"><path d="M2 1h2l1 2.5-1.3 1a6 6 0 0 0 2.8 2.8l1-1.3L10 7v2a1 1 0 0 1-1 1A9 9 0 0 1 0 2a1 1 0 0 1 1-1z"/></svg>
        000 000 0000
      </li>
      <li>
        <svg viewBox="0 0 10 10" aria-hidden="true"><path d="M0 2h10v6H0zM.8 2.6 5 5.6l4.2-3v-.1H.8z" fill-rule="evenodd"/></svg>
        youremail@domain.com
      </li>
      <li>
        <svg viewBox="0 0 10 10" aria-hidden="true"><path d="M5 0a5 5 0 1 0 0 10A5 5 0 0 0 5 0zm0 1c.6.6 1.1 1.7 1.3 3H3.7C3.9 2.7 4.4 1.6 5 1zM1.1 4.5h1.8a9 9 0 0 0 .4 3.9A4 4 0 0 1 1.1 5.5zm5.6 3.9a9 9 0 0 0 .4-3.9h1.8a4 4 0 0 1-2.2 3.9zM3.8 5h2.4c0 1.4-.5 2.9-1.2 3.8C4.3 7.9 3.8 6.4 3.8 5z"/></svg>
        yourwebsite.com
      </li>
    </ul>
  </section>

  <section class="card card-back" aria-label="Card back">
    <span class="brand-square" aria-hidden="true"></span>
    <p class="brand-name">Reid Calder</p>
  </section>

</main>
</body>
</html>
```